TOLLEN Naturals

We need a label design for a new online business. Our business is based in Georgia, developing a unique blend of botanicals and clay (bentonite clay) to cleanse natural (not chemically treated) hair. I would like to see designs for our Mud mask, which has 4 different scents (mild minty, faintly floral, hippiegrove and Plain 'Ol mud). The container is a clear 12 oz. jar( height:2.632in/6.685cm diameter: 3.688 in/9.368cm) with a white lid (height: 0.574in/1.458cm diameter: 3.662in/9.301cm).
We are looking for a rich, colorful, eye catching label that also matches the colors of the logo.
The products should have Tollen Naturals as its brand and should state what it is and what its for, for instance- Mud Mask for the hair, Mud for the hair or hair Mud.

Reason: I would like more designs.

Thank you all for your participation.

Target Market(s)

Individuals with thick, curly hair

Industry/Entity Type

Business

Colors

Designer to choose colors to be used in the design.

Requirements
Must have
• The label must be able to distinguish between the four different scents. For instance, adding a different feature to distinguish each scent.
Nice to have
• Logo with Tollen Naturals
Natural images ( floral - flowers, minty- leaves, hippie- peace)
Should not have
• Do not include "photo" of a woman

```html
<!DOCTYPE html>
<html lang="en">
<head>
<meta charset="utf-8">
<title>TOLLEN Naturals – Mud Mask Labels</title>
<link rel="stylesheet" href="https://fonts.googleapis.com/css2?family=Baloo+2:wght@600;700&family=Libre+Baskerville:wght@700&display=swap">
<style>
  :root {
    --page: #ffffff;
    --band-minty: #cdcbca;
    --band-floral: #6aacaa;
    --band-hippie: #5f9f1b;
    --band-plain: #2e2e04;
    --label-white: #f6f7fb;
    --brand-green: #2f8f6a;
    --title-gold: #b3a24a;
    --title-edge: #4a4216;
    --small-ink: #222222;
    --cream: #efe08a;
    --leaf: #4fae2a;
    --flower: #c23a4a;
  }
  html, body {
    margin: 0;
    padding: 0;
    width: 1200px;
    height: 852px;
    overflow: hidden;
    background: var(--page);
  }
  .label-sheet { display: block; width: 1200px; height: 852px; }
  .band--minty { fill: var(--band-minty); }
  .band--floral { fill: var(--band-floral); }
  .band--hippie { fill: var(--band-hippie); }
  .band--plain { fill: var(--band-plain); }
  .label-face { fill: var(--label-white); }
  .label-frame { fill: none; stroke: url(#silver); stroke-width: 7; }
  .brand-name {
    font-family: "Baloo 2", sans-serif;
    font-weight: 600;
    fill: var(--brand-green);
  }
  .product-title {
    font-family: "Baloo 2", sans-serif;
    font-weight: 700;
    font-size: 27px;
    fill: var(--title-gold);
    stroke: var(--title-edge);
    stroke-width: 0.8px;
  }
  .jar-note {
    font-family: "Libre Baskerville", serif;
    font-weight: 700;
    font-size: 7.5px;
    fill: var(--small-ink);
  }
</style>
</head>
<body>
<svg class="label-sheet" viewBox="0 0 1200 852" xmlns="http://www.w3.org/2000/svg">
  <defs>
    <filter id="soft-shadow" x="-5%" y="-20%" width="110%" height="140%">
      <feDropShadow dx="0" dy="2" stdDeviation="4" flood-color="#000" flood-opacity="0.35"/>
    </filter>
    <linearGradient id="silver" x1="0" y1="0" x2="1" y2="1">
      <stop offset="0" stop-color="#f4f4f4"/>
      <stop offset="0.35" stop-color="#8a8a8a"/>
      <stop offset="0.6" stop-color="#ffffff"/>
      <stop offset="1" stop-color="#6e6e6e"/>
    </linearGradient>
    <radialGradient id="cream-tone" cx="0.4" cy="0.4" r="0.7">
      <stop offset="0" stop-color="#f8eeaa"/>
      <stop offset="1" stop-color="#e3cf6a"/>
    </radialGradient>
    <linearGradient id="leaf-tone" x1="0" y1="0" x2="1" y2="1">
      <stop offset="0" stop-color="#7ccf3a"/>
      <stop offset="1" stop-color="#2f8a1e"/>
    </linearGradient>
    <radialGradient id="flower-tone" cx="0.5" cy="0.5" r="0.6">
      <stop offset="0" stop-color="#e56a7a"/>
      <stop offset="1" stop-color="#9a1f2e"/>
    </radialGradient>
    <clipPath id="label-clip">
      <path d="M42,3 H262 C288,3 300,40 309,108 C314,150 300,177 288,177 H30 C14,177 4,150 5,108 C6,58 16,3 42,3 Z"/>
    </clipPath>
    <symbol id="mud-mask-label" viewBox="0 0 320 180">
      <g filter="url(#soft-shadow)">
        <path class="label-face" d="M42,3 H262 C288,3 300,40 309,108 C314,150 300,177 288,177 H30 C14,177 4,150 5,108 C6,58 16,3 42,3 Z"/>
      </g>
      <g clip-path="url(#label-clip)">
        <path role="img" aria-label="Leaves with water droplets" fill="url(#leaf-tone)" d="M60,90 C90,60 110,55 130,62 C130,90 120,110 100,120 L190,150 C210,140 230,150 240,178 H90 Z"/>
        <path role="img" aria-label="Bowl of pale yellow hair cream" fill="url(#cream-tone)" d="M0,90 C30,82 80,84 98,96 C104,120 100,160 80,178 H0 Z"/>
        <path role="img" aria-label="Bouquet of red and pink roses" fill="url(#flower-tone)" d="M222,78 C250,70 280,85 292,110 C300,140 290,170 280,178 H212 C205,150 200,100 222,78 Z"/>
      </g>
      <path class="label-frame" d="M42,3 H262 C288,3 300,40 309,108 C314,150 300,177 288,177 H30 C14,177 4,150 5,108 C6,58 16,3 42,3 Z"/>
      <text class="brand-name" x="160" y="72" text-anchor="middle" font-size="30">TOLLEN</text>
      <text class="brand-name" x="160" y="87" text-anchor="middle" font-size="12">Naturals</text>
      <text class="product-title" x="168" y="113" text-anchor="middle">Mud Mask</text>
      <text class="product-title" x="160" y="136" text-anchor="middle">for the hair</text>
      <text class="jar-note" x="88" y="158" text-anchor="middle">100%</text>
      <text class="jar-note" x="88" y="166" text-anchor="middle">Organic</text>
      <text class="jar-note" x="88" y="174" text-anchor="middle">12 oz. Jar.</text>
    </symbol>
  </defs>

  <g class="scent scent--minty">
    <rect class="band--minty" x="12" y="12" width="1173" height="178" filter="url(#soft-shadow)"/>
    <use href="#mud-mask-label" x="185" y="11" width="320" height="180"/>
    <use href="#mud-mask-label" x="692" y="11" width="320" height="180"/>
  </g>
  <g class="scent scent--floral">
    <rect class="band--floral" x="12" y="233" width="1173" height="178" filter="url(#soft-shadow)"/>
    <use href="#mud-mask-label" x="196" y="232" width="320" height="180"/>
    <use href="#mud-mask-label" x="703" y="232" width="320" height="180"/>
  </g>
  <g class="scent scent--hippie">
    <rect class="band--hippie" x="12" y="448" width="1173" height="178" filter="url(#soft-shadow)"/>
    <use href="#mud-mask-label" x="196" y="447" width="320" height="180"/>
    <use href="#mud-mask-label" x="703" y="447" width="320" height="180"/>
  </g>
  <g class="scent scent--plain">
    <rect class="band--plain" x="12" y="661" width="1173" height="178" filter="url(#soft-shadow)"/>
    <use href="#mud-mask-label" x="196" y="660" width="320" height="180"/>
    <use href="#mud-mask-label" x="703" y="660" width="320" height="180"/>
  </g>
</svg>
</body>
</html>
```